Cover-Design für Buchprojekt
kiwano suchte ein neues Design in der Kategorie Buch-/eBook-Cover und hat ein Projekt auf entwurfsbuero.de gestartet.
Das sagt der Auftraggeber
Vielen Dank für das wunderbare, moderne Design unseres Buchcovers. Ihre Freundlichkeit, Schnelligkeit und Geduld bei der Ausarbeitung war sehr professionell. Wir empfehlen Sie gerne weiter und speichern Ihr Profil für das nächste Projekt. kiwano
Zielgruppe
Wir benötigen ein Cover für ein Buchprojekt, in dem es um Geld sparen für Kinder in Aktien/ETFs geht.
Eltern/Großeltern/Onkel/Tanten möchten Geld ansparen für ihr Kind, wissen aber, dass ein Sparbuch heutzutage aufgrund der niedrigen Zinsen keine gute Möglichkeit ist, haben schon von ETFs gehört (oder legen selber an) und möchten nun auch ein Depot für ihr Kind (Enkelkind, Nichte, Neffe) anlegen.
Zielgruppe:
1. Eltern (eher Mütter), die sich bereits selbst mit dem Thema Geldanlage beschäftigt haben, die selbst bereits ein ETF-Depot zur Altersvorsorge haben und nun überlegen, wie sie für ihr Kind/Kinder diese Vorteile auch nutzen können.
2 Eltern, bei denen Verwandte (Großeltern/Tanten/Onkel) den Wunsch haben, für die Kinder Geld anzusparen für die Zukunft. Doch diese möchten in einen Aktienfonds bei der Bank investieren, die Eltern kennen sich mit modernen Formen der Geldanlage aus und finden es sinnvoller, einen ETF-Depot fürs Kind einzurichten. Nun möchten sie die Verwandten mit diesem Buch davon überzeugen.
- Welche Probleme und Herausforderungen hat diese Zielgruppe?
Sie sind finanziell recht stabil aufgestellt und machen sich nun Gedanken um die Zukunft ihrer Kinder. Als Sicherheit möchten sie auch für ihre Kinder sparen. Sei es, um später mal ein Studium/Ausbildung zu finanzieren (eine „gute“ Ausbildung, womöglich auch ein Auslandssemester zu ermöglichen), den Führerschein, die erste eigene Wohnung oder einfach nur als Finanzpolster, wenn mal „was passiert“.
- Welche Ziele verfolgt deine Zielgruppe?
Sie möchten Sicherheit und Wohlstand für ihre Kinder/Enkel.
Sie möchten trotz Niedrigzinsumfeld das Geld fürs Kind sicher und gewinnbringend in ETFs anlegen.
Aufgabenstellung
Hochwertiges, modernes, minimalistisches Design, das sich von der Masse abhebt. Keine Aktiencharts. Keine Pflanzen, die wachsen oder gegossen werden. Gerne ein Design, das Sicherheit fürs Kind vermittelt (kein Muss). Keine Personen frontal. Wirkung wie ein seriöser Ratgeber (z.B. wie Ratgeber vom RT Verlag oder PW).
Autor: Konstantin Brugger
Titel/Untertitel: Unser Nachwuchs baut früh Vermögen auf. Wie Eltern sicher in ETFs sparen, Fallstricke von Anfang an vermeiden und ein Geld-Mindset prägen
Backcover und Buchrücken wird benötigt (dies erst im nächsten Schritt, Backcovertext wird dann gegeben)
Format Taschenbuch: 5x8

```html
<!DOCTYPE html>
<html lang="de">
<head>
<meta charset="utf-8">
<title>Unser Nachwuchs baut früh Vermögen auf – Cover</title>
<link rel="stylesheet" href="https://fonts.googleapis.com/css2?family=Comfortaa:wght@300;400&family=Quicksand:wght@400;500&display=swap">
<style>
  :root {
    --paper: #ffffff;
    --rose: #e1aea3;
    --rose-deep: #d89c90;
    --sand: #ecdccd;
    --ink: #141414;
    --white: #ffffff;
  }
  html, body {
    margin: 0;
    padding: 0;
    width: 848px;
    height: 1200px;
    overflow: hidden;
    background: var(--paper);
  }
  .cover {
    position: relative;
    width: 848px;
    height: 1200px;
    overflow: hidden;
    background: var(--paper);
    font-family: "Quicksand", sans-serif;
  }
  .cover__art {
    position: absolute;
    inset: 0;
  }
  .author {
    position: absolute;
    top: 50px;
    left: 0;
    width: 848px;
    text-align: center;
    font-family: "Quicksand", sans-serif;
    font-weight: 500;
    font-size: 27px;
    color: var(--ink);
    letter-spacing: -0.2px;
  }
  .title { margin: 0; font-weight: 300; }
  .title__line {
    position: absolute;
    white-space: nowrap;
    line-height: 1;
  }
  .title__caps {
    font-family: "Quicksand", sans-serif;
    font-weight: 400;
    text-transform: uppercase;
    letter-spacing: 1px;
  }
  .title__big {
    font-family: "Comfortaa", sans-serif;
    font-weight: 300;
    letter-spacing: -3px;
  }
  .title__line--one {
    left: 58px;
    top: 622px;
    color: var(--ink);
  }
  .title__line--one .title__caps { font-size: 46px; margin-right: 14px; }
  .title__line--one .title__big { font-size: 104px; }
  .title__line--two {
    right: 14px;
    top: 800px;
    color: var(--ink);
    font-size: 52px;
  }
  .title__line--three {
    left: 100px;
    top: 880px;
    color: var(--white);
  }
  .title__line--three .title__big { font-size: 122px; margin-right: 22px; }
  .title__line--three .title__caps { font-size: 50px; color: var(--ink); }
  .subtitle {
    position: absolute;
    left: 60px;
    width: 728px;
    top: 1088px;
    margin: 0;
    text-align: center;
    font-family: "Quicksand", sans-serif;
    font-weight: 500;
    font-size: 22px;
    line-height: 29px;
    color: var(--ink);
  }
</style>
</head>
<body>
<main class="cover">
  <svg class="cover__art" width="848" height="1200" viewBox="0 0 848 1200" xmlns="http://www.w3.org/2000/svg">
    <defs>
      <linearGradient id="illustration-tone" x1="0" y1="0" x2="0" y2="1">
        <stop offset="0" stop-color="#ecdccd"/>
        <stop offset="0.55" stop-color="#e6c3b6"/>
        <stop offset="1" stop-color="#ecdccd"/>
      </linearGradient>
    </defs>
    <rect class="cover__illustration" x="160" y="0" width="660" height="560" rx="24"
          fill="url(#illustration-tone)" role="img"
          aria-label="Illustration: zwei Händepaare halten schützend ein rosafarbenes Sparschwein"/>
    <polygon class="cover__rose-band" fill="var(--rose)"
      points="0,880 57,791 77,820 118,775 148,768 653,763 690,615 715,662 748,452 770,538 810,188 826,227 848,196 848,1200 0,1200"/>
  </svg>

  <div class="author">Konstantin Brugger</div>

  <h1 class="title">
    <span class="title__line title__line--one"><span class="title__caps">Unser</span><span class="title__big">Nachwuchs</span></span>
    <span class="title__line title__line--two title__caps">Baut früh</span>
    <span class="title__line title__line--three"><span class="title__big">Vermögen</span><span class="title__caps">auf</span></span>
  </h1>

  <p class="subtitle">Wie Eltern sicher in ETFs sparen, Fallstricke von Anfang<br>an vermeiden und ein Geld-Mindset prägen</p>
</main>
</body>
</html>
```